Bright Horizon Website

Bright Horizon Advisory Services is a company which provides specialised advise in carbon markets, climate policy, landscapes, resilience and change. We are based in Australia but the majority of our business is global. Our clients range from governments to large corporates and not for profit organisations.
Our focus is on developing the capabilities of government officials, business decision makers and land managers so they can better navigate the complexity of climate change and sustainability.
We are looking for a website that is consistent with the high end professional services which we provide to serious players.
I have attached two versions of our logo. I have also attached the back of our business card so you can get a sense of what we hand to potential clients.

Target Market(s)

Professional individuals, decision makers, board members etc, government officials.

Industry/Entity Type

Government

Number of Pages Required

4 page

Font styles to use
Serif
Sans Serif

Requirements
Must have
• Please provide
• 1. Home page
• 2. Service page template
• 3. Contact page
• 4. Lead expert profile page

```html
<!DOCTYPE html>
<html lang="en">
<head>
<meta charset="utf-8">
<title>Bright Horizon Website</title>
<link rel="stylesheet" href="https://fonts.googleapis.com/css2?family=Lora:wght@400;700&family=Arimo:wght@400;700&display=swap">
<style>
:root{
  --page:#f2f2f2;
  --white:#ffffff;
  --slate:#4a4d55;
  --ink:#3d3d3d;
  --muted:#8a8a8a;
  --faint:#b5b5b5;
  --line:#e3e3e3;
  --blue:#1f8ac7;
  --red:#f0523e;
  --orange:#f26b22;
  --amber:#f5a31a;
  --green:#35bc7a;
  --pin:#e02b2b;
  --fb:#3b5a98;
  --tw:#35a7dc;
  --gp:#e14a3a;
  --serif:'Lora', Georgia, serif;
  --sans:'Arimo', Arial, sans-serif;
}
*{box-sizing:border-box;margin:0;padding:0}
html,body{width:930px;height:1200px;overflow:hidden}
body{background:var(--page);font-family:var(--sans);color:var(--ink);position:relative}
.abs{position:absolute}

/* top bar */
.topbar{left:0;top:0;width:930px;height:26px;background:var(--white);font-family:var(--serif);font-size:9px;color:var(--muted)}
.topbar .contact-item{top:8px;display:flex;align-items:center;gap:6px;white-space:nowrap}
.topbar .divider{left:231px;top:7px;width:1px;height:12px;background:var(--line)}
.topbar .social{top:8px;width:9px;height:9px;border-radius:50%;background:#c8c8c8}

/* header */
.brand{left:135px;top:45px;width:242px;height:77px;background:var(--slate);display:flex;align-items:center;justify-content:center;gap:10px;color:var(--white);font-family:var(--serif);font-size:18px;letter-spacing:2px;text-transform:uppercase;white-space:nowrap}
.brand .mark{width:26px;height:26px;border-radius:50%;border:2px solid #d8d8d8}
.nav-item{top:45px;height:77px;background:var(--white);border:1px solid #ececec;font-family:var(--serif);font-size:11.5px;text-transform:uppercase;text-align:center;padding-top:18px;white-space:nowrap}
.nav-item svg{display:block;margin:0 auto 6px}
.nav-item.active{border-top:4px solid var(--blue);border-bottom:4px solid var(--blue);padding-top:14px;color:var(--blue)}

/* hero */
.hero-photo{left:135px;top:142px;width:467px;height:200px;background:linear-gradient(135deg,#e9ecef 0%,#c9ced4 45%,#5d6470 75%,#2f3540 100%)}
.hero-panel{left:602px;top:142px;width:194px;height:200px;background:var(--white);padding:14px 14px}
.hero-panel .kicker{display:flex;align-items:center;gap:10px;font-family:var(--serif);font-weight:700;font-size:11px;text-transform:uppercase;color:var(--ink);padding-bottom:9px;border-bottom:1px solid var(--line);white-space:nowrap}
.hero-panel h2{font-family:var(--serif);font-weight:400;font-size:15px;letter-spacing:-.1px;color:var(--blue);margin:8px 0 8px;text-transform:uppercase;white-space:nowrap}
.hero-panel ul{list-style:none;font-family:var(--serif);font-size:11.5px;color:#8b8b8b}
.hero-panel li{margin-bottom:5px;padding-left:14px;position:relative;white-space:nowrap}
.hero-panel li::before{content:'›';position:absolute;left:0;top:-2px;font-size:15px;color:#b0b0b0}
.btn-more{right:13px;bottom:14px;width:65px;height:25px;background:var(--slate);color:var(--white);font-family:var(--serif);font-size:9px;display:flex;align-items:center;justify-content:center;text-transform:uppercase}

/* feature cards */
.feature{top:365px;height:237px;color:var(--white);padding:20px 19px}
.feature h3{font-family:var(--serif);font-weight:700;font-size:15px;margin:15px 0 8px;text-transform:uppercase;white-space:nowrap}
.feature p{font-size:8.5px;line-height:10.4px;max-height:63px;overflow:hidden}
.feature .go{right:20px;bottom:20px;width:30px;height:30px;border-radius:50%;border:2px solid rgba(255,255,255,.4)}
.red{background:var(--red)}.blue{background:var(--blue)}.green{background:var(--green)}

/* projects */
.projects{left:135px;top:625px;width:662px;height:257px;background:var(--white)}
.section-title{font-family:var(--serif);font-weight:700;font-size:17px;text-transform:uppercase;color:var(--ink);white-space:nowrap}
.section-sub{font-size:11px;color:var(--muted);white-space:nowrap}
.project{top:76px;width:153px;height:155px}
.project .label{left:0;bottom:0;width:100%;height:31px;background:rgba(80,80,80,.85);color:var(--white);font-family:var(--serif);font-size:11.5px;text-transform:uppercase;display:flex;align-items:center;justify-content:center;white-space:nowrap}
.project-detail{background:#5d5e60;color:var(--white);padding:16px 18px}
.project-detail h4{font-family:var(--serif);font-weight:700;font-size:11.5px;text-transform:uppercase;padding-bottom:5px;border-bottom:1px solid rgba(255,255,255,.5);width:112px;white-space:nowrap}
.project-detail p{font-size:8.5px;line-height:10.3px;font-weight:700;margin-top:8px;max-height:52px;overflow:hidden}

/* advisory */
.advisory{left:135px;top:909px;width:662px;height:190px;background:var(--white)}
.team-photo{left:15px;top:18px;width:258px;height:172px;background:linear-gradient(180deg,#f4f4f4 0%,#cfd2d6 40%,#6b6f77 100%)}
.service{width:160px;display:flex;gap:11px}
.service .ring{flex:none;width:34px;height:34px;border-radius:50%;border:2px solid;display:flex;align-items:center;justify-content:center}
.service h5{font-family:var(--serif);font-weight:400;font-size:12.5px;margin-top:-3px;white-space:nowrap}
.service p{font-size:8.5px;line-height:11px;color:var(--faint)}

/* footer */
.footer{left:0;top:1127px;width:930px;height:73px;background:var(--white)}
.footer .legal{left:136px;top:29px;font-family:var(--serif);font-size:11px;color:var(--ink);white-space:nowrap}
.footer .footer-brand{left:437px;top:22px;display:flex;align-items:center;gap:6px;font-family:var(--serif);font-size:11px;color:var(--muted);white-space:nowrap}
.footer .footer-brand .mark{width:24px;height:24px;border-radius:50%;border:2px solid #b8b8b8}
.footer .social{top:26px;width:22px;height:22px;border-radius:50%}
</style>
</head>
<body>

<div class="abs topbar">
  <div class="abs contact-item" style="left:135px">
    <svg width="10" height="10" viewBox="0 0 10 10"><path d="M2 1l2 2-1 1.5c.7 1.3 1.5 2 2.5 2.5L7 6l2 2-1.5 1.5C4 9 1 6 .5 2.5z" fill="#b0b0b0"/></svg>
    0800 (555) 0199
  </div>
  <div class="abs divider"></div>
  <div class="abs contact-item" style="left:243px">
    <svg width="12" height="9" viewBox="0 0 12 9"><rect x=".5" y=".5" width="11" height="8" fill="none" stroke="#b0b0b0"/><path d="M.5.5l5.5 4.5 5.5-4.5" fill="none" stroke="#b0b0b0"/></svg>
    hello@brighthorizon.example
  </div>
  <div class="abs social" style="left:716px"></div>
  <div class="abs social" style="left:739px"></div>
  <div class="abs social" style="left:763px"></div>
  <div class="abs social" style="left:787px"></div>
</div>

<header>
  <div class="abs brand"><span class="mark"></span>Bright Horizon</div>
  <nav>
    <div class="abs nav-item active" style="left:383px;width:79px">
      <svg width="24" height="22" viewBox="0 0 24 22"><path d="M12 1L1 11h3v10h6v-6h4v6h6V11h3z" fill="var(--blue)"/></svg>Home
    </div>
    <div class="abs nav-item" style="left:469px;width:76px;color:var(--orange)">
      <svg width="24" height="24" viewBox="0 0 24 24"><circle cx="14" cy="4" r="3" fill="var(--orange)"/><path d="M9 10h7l-3 10h3l-1 2H7l3-10H8z" fill="var(--orange)"/></svg>About
    </div>
    <div class="abs nav-item" style="left:552px;width:77px;color:var(--amber)">
      <svg width="26" height="24" viewBox="0 0 26 24"><circle cx="9" cy="10" r="6" fill="none" stroke="var(--amber)" stroke-width="3" stroke-dasharray="3 2"/><circle cx="19" cy="18" r="4" fill="none" stroke="var(--amber)" stroke-width="2.5" stroke-dasharray="2.5 1.5"/></svg>Services
    </div>
    <div class="abs nav-item" style="left:636px;width:76px;color:var(--green)">
      <svg width="24" height="24" viewBox="0 0 24 24"><circle cx="10" cy="6" r="5" fill="var(--green)"/><path d="M1 23c0-7 4-10 9-10s6 2 7 4l-4 6z" fill="var(--green)"/><path d="M15 22l6-8 2 2-6 8h-2z" fill="var(--green)"/></svg>Profile
    </div>
    <div class="abs nav-item" style="left:719px;width:77px;color:var(--red)">
      <svg width="26" height="24" viewBox="0 0 26 24"><path d="M4 14v-3a9 9 0 0118 0v3" fill="none" stroke="var(--red)" stroke-width="2.5"/><rect x="2" y="12" width="5" height="8" rx="2" fill="var(--red)"/><rect x="19" y="12" width="5" height="8" rx="2" fill="var(--red)"/></svg>Contact
    </div>
  </nav>
</header>

<main>
  <div class="abs hero-photo" role="img" aria-label="Photo of a business team meeting around a boardroom table"></div>
  <aside class="abs hero-panel">
    <div class="kicker">
      <svg width="20" height="20" viewBox="0 0 20 20"><circle cx="10" cy="10" r="8.5" fill="none" stroke="var(--ink)" stroke-width="2"/><path d="M8.5 6l4 4-4 4" fill="none" stroke="var(--ink)" stroke-width="2"/></svg>
      Bright Horizon
    </div>
    <h2>Advisory Services</h2>
    <ul>
      <li>Carbon Markets</li>
      <li>Climate Policy</li>
      <li>Landscapes</li>
      <li>Resilience</li>
    </ul>
    <div class="abs btn-more">More</div>
  </aside>

  <section class="abs feature red" style="left:134px;width:216px">
    <svg width="48" height="48" viewBox="0 0 48 48" fill="none" stroke="#fff" stroke-width="2"><path d="M17 30a11 11 0 1114 0v5H17z"/><path d="M19 39h10M20 43h8"/><path d="M24 3v5M6 21h5M37 21h5M11 8l3 3M37 8l-3 3"/></svg>
    <h3>Creative Solutions</h3>
    <p>Lorem ipsum dolor sit amet, consectetuer the adipiscing elit, sed diam nonummy nibh btray euismod tincidunt ut laoreet dolore magna mi aliquam erat volutpat. Ut wisi enim ad minixz veniam, quis nostrud exerci tation ullamcorpt suscipit lobortis nisl ut aliquip ex ea comm...</p>
    <div class="abs go"></div>
  </section>
  <section class="abs feature blue" style="left:358px;width:215px">
    <svg width="52" height="48" viewBox="0 0 52 48" fill="none" stroke="#fff" stroke-width="2"><path d="M8 22a18 18 0 0130-13M44 26a18 18 0 01-30 13"/><path d="M38 3v7h-7M14 45v-7h7"/><circle cx="22" cy="22" r="6" stroke-dasharray="3 2" stroke-width="3"/><circle cx="32" cy="30" r="4" stroke-dasharray="2 2" stroke-width="3"/></svg>
    <h3>Featured Services</h3>
    <p>Lorem ipsum dolor sit amet, consectetuer the adipiscing elit, sed diam nonummy nibh btray euismod tincidunt ut laoreet dolore magna mi aliquam erat volutpat. Ut wisi enim ad minixz veniam, quis nostrud exerci tation ullamcorpt suscipit lobortis nisl ut aliquip ex ea comm...</p>
    <div class="abs go"></div>
  </section>
  <section class="abs feature green" style="left:581px;width:216px">
    <svg width="50" height="48" viewBox="0 0 50 48" fill="none" stroke="#fff" stroke-width="2"><circle cx="25" cy="24" r="15"/><path d="M6 24a19 19 0 0138 0"/><rect x="3" y="20" width="6" height="11" rx="2" fill="#fff"/><rect x="41" y="20" width="6" height="11" rx="2" fill="#fff"/><path d="M44 31c0 8-6 11-14 11"/></svg>
    <h3>Technical Support</h3>
    <p>Lorem ipsum dolor sit amet, consectetuer the adipiscing elit, sed diam nonummy nibh btray euismod tincidunt ut laoreet dolore magna mi aliquam erat volutpat. Ut wisi enim ad minixz veniam, quis nostrud exerci tation ullamcorpt suscipit lobortis nisl ut aliquip ex ea comm...</p>
    <div class="abs go"></div>
  </section>

  <section class="abs projects">
    <h2 class="abs section-title" style="left:0;top:22px;width:100%;text-align:center">Bright Horizon Projects</h2>
    <p class="abs section-sub" style="left:0;top:45px;width:100%;text-align:center">Bright Horizon Advisory Services</p>

    <div class="abs project" style="left:17px;background:linear-gradient(160deg,#eef0f2,#b9bec4)" role="img" aria-label="Photo of colleagues reviewing documents together">
      <div class="abs label">Landscapes</div>
    </div>
    <div class="abs project" style="left:175px;background:linear-gradient(160deg,#9fb6c4,#4c5964)" role="img" aria-label="Photo of professionals looking upward in a glass building">
      <div class="abs label">Climate Policy</div>
    </div>
    <div class="abs project" style="left:333px;background:linear-gradient(160deg,#e8e4df,#9a9590)" role="img" aria-label="Photo of a team discussing work at a desk">
      <div class="abs label">Resilience</div>
    </div>
    <div class="abs project project-detail" style="left:491px">
      <h4>Carbon Markets</h4>
      <p>Lorem ipsum dolor sit amet, consectetuer the adipiscing elit, sed diam nonummy nibh btray euismod tincidu laoreet dolore magna mi aliquam....</p>
      <svg class="abs" style="left:19px;bottom:20px" width="20" height="20" viewBox="0 0 20 20"><circle cx="10" cy="10" r="8.5" fill="none" stroke="#fff" stroke-width="2"/><path d="M8.5 6l4 4-4 4" fill="none" stroke="#fff" stroke-width="2"/></svg>
    </div>
  </section>

  <section class="abs advisory">
    <div class="abs team-photo" role="img" aria-label="Photo of a large group of smiling business people"></div>
    <h2 class="abs section-title" style="left:306px;top:27px;font-size:15px">Bright Horizon Advisory Services</h2>
    <p class="abs section-sub" style="left:307px;top:49px">Advisory Services !</p>

    <div class="abs service" style="left:306px;top:78px">
      <div class="ring" style="border-color:var(--blue)"><svg width="14" height="18" viewBox="0 0 14 18" fill="none" stroke="var(--blue)" stroke-width="1.5"><path d="M4 12a6 6 0 116 0v2H4zM5 16h4"/></svg></div>
      <div><h5 style="color:var(--blue)">Resilience</h5><p>Lorem ipsum dolor sit amet, consectetuer the adipisci....</p></div>
    </div>
    <div class="abs service" style="left:481px;top:78px">
      <div class="ring" style="border-color:var(--orange)"><svg width="16" height="14" viewBox="0 0 16 14"><path d="M1 13l5-8 3 5 2-3 4 6z" fill="var(--orange)"/><circle cx="11" cy="3" r="2" fill="var(--orange)"/></svg></div>
      <div><h5 style="color:var(--orange)">Landscapes</h5><p>Lorem ipsum dolor sit amet, consectetuer the adipisci....</p></div>
    </div>
    <div class="abs service" style="left:306px;top:128px">
      <div class="ring" style="border-color:var(--red)"><svg width="16" height="16" viewBox="0 0 16 16"><path d="M2 15h12V8l-3 2V7l-3 2V3H5v12" fill="var(--red)"/></svg></div>
      <div><h5 style="color:var(--red)">Carbon Markets</h5><p>Lorem ipsum dolor sit amet, consectetuer the adipisci....</p></div>
    </div>
    <div class="abs service" style="left:481px;top:128px">
      <div class="ring" style="border-color:var(--green)"><svg width="18" height="14" viewBox="0 0 18 14"><path d="M1 6c3-5 13-5 16 0-3 2-13 2-16 0zM5 9h8l-2 4H7z" fill="var(--green)"/></svg></div>
      <div><h5 style="color:var(--green)">Climate Policy</h5><p>Lorem ipsum dolor sit amet, consectetuer the adipisci....</p></div>
    </div>
  </section>
</main>

<footer class="abs footer">
  <p class="abs legal">Bright Horizon © 2014 Privacy Policy</p>
  <div class="abs footer-brand"><span class="mark"></span>Bright Horizon</div>
  <span class="abs social" style="left:683px;background:var(--fb)"></span>
  <span class="abs social" style="left:713px;background:var(--tw)"></span>
  <span class="abs social" style="left:744px;background:var(--gp)"></span>
  <span class="abs social" style="left:774px;background:var(--pin)"></span>
</footer>

</body>
</html>
```